*YO!!! Designers Needed!!* Front Page Cover Needed for a $$Billion Dollar$$ Company

We are a manufacturer of aluminum electrolytic capacitors. We are looking to create a front page cover that will be used on our annual report. We are a publicly listed company and work with many Pinnacle 300 companies, so your work will be viewed by the BIG GUNS and EXECUTIVES around the WORLD! If selected, you may be selected for additional work.

The front page cover should be unique. If elegance, modern, bling, and creativity somehow got together and had a child, that's what the cover page would look like!

Inspired Examples attached. Check them out!

www.velmoro.com

Font styles to use
Sans Serif

Requirements
Must have
• 1. Must include the attached logo. Logo size, color, and placement are at your discretion.

2. Should include the text, '2020 Annual Report'

3. The design should incorporate the use of foil and/or be embossed. The foil can be part of the design or can be the full page. See various examples attached for reference.

4. Shall be in A4 size and vertical orientation.
Nice to have
• Feel free to add any icons or stock photos (for example capacitors or circuit boards) if needed.

Be creative here and don't be afraid to be bold! The end product will be printed and budget is not a limiting factor, so feel free to make it extravagant if needed.

Our slogan is "Think Ahead". This slogan can or cannot be part of the theme.

```html
<!DOCTYPE html>
<html lang="en">
<head>
<meta charset="UTF-8">
<title>Velmoro 2020 Annual Report Cover</title>
<link href="https://fonts.googleapis.com/css2?family=Montserrat:wght@800;900&family=Lato:wght@700&display=swap" rel="stylesheet">
<style>
  :root {
    --backdrop: #2a3233;
    --paper: #ffffff;
    --cream: #f1ecdc;
    --cream-soft: #f8f5ec;
    --ink: #0d0d0d;
    --gold-light: #f0d64a;
    --gold-mid: #d9b22a;
    --gold-deep: #b48a1c;
  }
  * { margin: 0; padding: 0; box-sizing: border-box; }
  html, body {
    width: 1200px;
    height: 1200px;
    overflow: hidden;
    background: var(--backdrop);
  }
  .cover {
    position: absolute;
    left: 211px;
    top: 50px;
    width: 778px;
    height: 1100px;
    background: var(--paper);
    overflow: hidden;
  }
  .embossed-pattern {
    position: absolute;
    inset: 0;
    background: linear-gradient(180deg, var(--cream) 0%, var(--cream-soft) 35%, var(--paper) 55%, var(--paper) 85%, var(--cream-soft) 100%);
  }
  .foil-chevrons {
    position: absolute;
    inset: 0;
    width: 100%;
    height: 100%;
  }
  .title-rule {
    position: absolute;
    left: 20px;
    top: 82px;
    width: 21px;
    height: 282px;
    background: linear-gradient(180deg, var(--gold-deep), var(--gold-mid) 50%, var(--gold-deep));
  }
  .report-title {
    position: absolute;
    left: 55px;
    top: 78px;
    font-family: 'Montserrat', sans-serif;
    font-weight: 900;
    font-size: 74px;
    line-height: 78px;
    letter-spacing: 0.5px;
    color: var(--ink);
  }
  .report-title span { display: block; }
  .report-slogan {
    position: absolute;
    left: 63px;
    top: 330px;
    font-family: 'Lato', sans-serif;
    font-weight: 700;
    font-size: 32px;
    letter-spacing: -0.5px;
    color: var(--ink);
  }
  .brand {
    position: absolute;
    right: 188px;
    top: 920px;
    text-align: right;
    color: var(--ink);
  }
  .brand-name {
    font-family: 'Montserrat', sans-serif;
    font-weight: 800;
    font-size: 50px;
    line-height: 1;
    letter-spacing: 1px;
  }
  .brand-tagline {
    margin-top: 6px;
    font-family: 'Lato', sans-serif;
    font-weight: 700;
    font-size: 14px;
    letter-spacing: 0.5px;
  }
</style>
</head>
<body>
  <main class="cover">
    <div class="embossed-pattern" role="img" aria-label="Embossed pearl-cream pattern of concentric circles"></div>

    <svg class="foil-chevrons" viewBox="0 0 952 1345" preserveAspectRatio="none" aria-hidden="true">
      <defs>
        <linearGradient id="gold-foil" x1="0" y1="1" x2="1" y2="0">
          <stop offset="0" stop-color="#e2c232"/>
          <stop offset="0.45" stop-color="#f0d64a"/>
          <stop offset="0.75" stop-color="#d9b22a"/>
          <stop offset="1" stop-color="#c79c22"/>
        </linearGradient>
      </defs>
      <polygon class="chevron-upper" fill="url(#gold-foil)"
        points="0,1030 704,663 952,875 952,1015 684,765 0,1130"/>
      <polygon class="chevron-lower" fill="url(#gold-foil)"
        points="0,1175 684,815 952,1035 952,1200 662,935 0,1280"/>
    </svg>

    <div class="title-rule"></div>
    <h1 class="report-title">
      <span>2020</span>
      <span>ANNUAL</span>
      <span>REPORT</span>
    </h1>
    <p class="report-slogan">THINK AHEAD</p>

    <div class="brand">
      <div class="brand-name">VELMORO</div>
      <div class="brand-tagline">THINK AHEAD.</div>
    </div>
  </main>
</body>
</html>
```